Business Card for a new businees.

need a very good business for a new company based in Riverside California call Levy Lantern LLC. We help client file taxes, resolve tax debt and attain peace of mind We help people nationwide solve Tax problems. We help with Installment agreements, Offers in Compromise, Partial Pay Installment Agreements, Currently Not Collectible status, Liens and Levy Removal, Garnishment removal. We offer individualized services

Target Market(s)

Any one with Tax Problems nationwide. My clients span across age, occupation etc

Contact Information for Business Card

Card must be attractive and have enough information to let client know we care and call us

Colors

Designer to choose colors to be used in the design.

Requirements
Must have
• the basics and then surprise me
Nice to have
• surprise m

```html
<!DOCTYPE html>
<html lang="en">
<head>
<meta charset="utf-8">
<title>Levy Lantern LLC — Business Card</title>
<link href="https://fonts.googleapis.com/css2?family=Roboto:wght@400;500;700&display=swap" rel="stylesheet">
<style>
  :root {
    --backdrop: #5b4f47;
    --card: #141414;
    --card-edge: #1d1d1d;
    --gold: #f0c419;
    --gold-muted: #9c8428;
    --ink-light: #f2f2f2;
  }
  * { box-sizing: border-box; margin: 0; padding: 0; }
  html, body { width: 1200px; height: 716px; overflow: hidden; }
  body {
    background: var(--backdrop);
    font-family: "Roboto", Arial, sans-serif;
    position: relative;
  }
  .card {
    position: absolute;
    top: 200px;
    width: 540px;
    height: 316px;
    background: linear-gradient(160deg, var(--card-edge), var(--card) 60%);
    border-radius: 4px;
    overflow: hidden;
  }
  .card--front { left: 40px; }
  .card--back { left: 620px; }

  /* Front */
  .brand-mark {
    position: absolute;
    left: 50%;
    top: 88px;
    transform: translateX(-50%);
    display: flex;
    align-items: center;
    gap: 14px;
    white-space: nowrap;
  }
  .brand-mark__dot {
    width: 34px; height: 34px;
    border-radius: 50%;
    background: var(--gold);
  }
  .brand-mark__name {
    color: var(--gold);
    font-weight: 700;
    font-size: 34px;
  }
  .front-url {
    position: absolute;
    left: 0; right: 0;
    top: 196px;
    text-align: center;
    color: var(--gold);
    font-size: 19px;
  }

  /* Back */
  .back-brand {
    position: absolute;
    left: 40px;
    top: 40px;
    display: flex;
    align-items: center;
    gap: 10px;
  }
  .back-brand__dot {
    width: 22px; height: 22px;
    border-radius: 50%;
    background: var(--gold);
  }
  .back-brand__name {
    color: var(--gold);
    font-weight: 700;
    font-size: 24px;
  }
  .person {
    position: absolute;
    left: 40px;
    top: 104px;
  }
  .person__name {
    color: var(--gold);
    font-size: 20px;
    font-weight: 500;
  }
  .person__title {
    color: var(--gold-muted);
    font-size: 18px;
    margin-top: 2px;
  }
  .contact {
    position: absolute;
    right: 36px;
    top: 176px;
    width: 270px;
    color: var(--ink-light);
    font-size: 15px;
    line-height: 1.3;
  }
  .contact__address { padding-bottom: 6px; }
  .contact__rule {
    height: 2px;
    background: var(--gold);
    margin-bottom: 8px;
  }
  .contact__list { list-style: none; }
  .contact__item {
    display: flex;
    align-items: center;
    gap: 9px;
    line-height: 1.4;
  }
  .contact__icon { width: 13px; height: 13px; flex: none; fill: var(--gold); }
</style>
</head>
<body>

<section class="card card--front" aria-label="Card front">
  <div class="brand-mark">
    <span class="brand-mark__dot"></span>
    <span class="brand-mark__name">Levy Lantern LLC</span>
  </div>
  <p class="front-url">www.levylantern.com</p>
</section>

<section class="card card--back" aria-label="Card back">
  <div class="back-brand">
    <span class="back-brand__dot"></span>
    <span class="back-brand__name">Levy Lantern LLC</span>
  </div>

  <div class="person">
    <p class="person__name">Employee Name</p>
    <p class="person__title">Title</p>
  </div>

  <div class="contact">
    <p class="contact__address">4820 Orchard Ave. Ste 110<br>Riverside, CA 92506</p>
    <div class="contact__rule"></div>
    <ul class="contact__list">
      <li class="contact__item">
        <svg class="contact__icon" viewBox="0 0 16 16"><path d="M3 1h3l1.5 4-2 1.3a9 9 0 0 0 4.2 4.2L11 8.5l4 1.5v3a2 2 0 0 1-2 2A13 13 0 0 1 1 3a2 2 0 0 1 2-2z"/></svg>
        951-555-0148
      </li>
      <li class="contact__item">
        <svg class="contact__icon" viewBox="0 0 16 16"><path d="M4 0h8a1 1 0 0 1 1 1v14a1 1 0 0 1-1 1H4a1 1 0 0 1-1-1V1a1 1 0 0 1 1-1zm1 2v10h6V2zm3 11a1 1 0 1 0 0 2 1 1 0 0 0 0-2z"/></svg>
        951-555-0148
      </li>
      <li class="contact__item">
        <svg class="contact__icon" viewBox="0 0 16 16"><path d="M0 3h16v10H0zm1.5 1.2V12h13V4.2L8 9z"/></svg>
        info@levylantern.com
      </li>
      <li class="contact__item">
        <svg class="contact__icon" viewBox="0 0 16 16"><path d="M8 0a8 8 0 1 0 0 16A8 8 0 0 0 8 0zm0 1.5c.9 0 1.9 1.6 2.3 4.5H5.7C6.1 3.1 7.1 1.5 8 1.5zM1.6 7h2.9a15 15 0 0 0 0 2H1.6a6.5 6.5 0 0 1 0-2zm4 0h4.8a14 14 0 0 1 0 2H5.6a14 14 0 0 1 0-2zm5.9 0h2.9a6.5 6.5 0 0 1 0 2h-2.9a15 15 0 0 0 0-2zM5.7 10h4.6c-.4 2.9-1.4 4.5-2.3 4.5S6.1 12.9 5.7 10z"/></svg>
        www.levylantern.com
      </li>
    </ul>
  </div>
</section>

</body>
</html>
```